Zielgruppe
Die travlon GmbH bietet professionelle Cloud-Lösungen im Bereich spezialisierter Verwaltungssysteme. Hierbei handelt es sich um Software as a Service (SaaS), die zu 100% von der travlon GmbH betrieben und kontinuierlich weiterentwickelt wird.
Aufgabenstellung
Das Design kann Farben und/oder Elemente der travlon GmbH enthalten (www.travlon.de). Da es sich um ein eigenen Produkt handelt, muss jedoch auch Neutralität bewahrt werden.

```html
<!DOCTYPE html>
<html lang="de">
<head>
<meta charset="utf-8">
<title>Domora – Domain Liste</title>
<link href="https://fonts.googleapis.com/css2?family=Roboto:wght@400;500;700&display=swap" rel="stylesheet">
<style>
:root{
  --brand:#e11d27;
  --ink:#1c1c1c;
  --muted:#9a9a9a;
  --line:#d9d9d9;
  --soft:#f3f3f3;
  --ok:#16b98a;
  --white:#fff;
}
*{box-sizing:border-box;margin:0;padding:0}
html,body{width:1200px;height:675px;overflow:hidden;background:var(--white);font-family:'Roboto',sans-serif;color:var(--ink)}
.canvas{position:relative;width:1200px;height:675px}
.abs{position:absolute}
.topbar{position:absolute;left:0;top:0;width:1200px;height:62.5px;background:var(--brand);color:var(--white)}
.brand-name{left:174px;top:20px;font-size:17.5px;font-weight:500;letter-spacing:.2px}
.notice{font-size:8.75px;display:flex;align-items:center;gap:6px}
.meta{font-size:8.75px}
.session-user{font-size:8.75px;font-weight:700}
.session-bar{left:941px;top:30.5px;width:84px;height:4.5px;background:var(--white);border-radius:2px;overflow:hidden}
.session-bar span{display:block;width:60px;height:100%;background:var(--ok)}
.session-rest{font-size:7.5px}
.logout{font-size:8.75px;display:flex;align-items:center;gap:5px}
.mainnav{position:absolute;left:0;top:62.5px;width:1200px;height:35px;background:var(--soft)}
.mainnav a{position:absolute;top:12px;font-size:8.75px;font-weight:500;color:var(--ink);text-decoration:none}
.mainnav a.active{color:var(--brand)}
.mainnav a.active::after{content:"";position:absolute;left:0;right:0;top:20.5px;height:2px;background:var(--brand)}
.sidebar{left:175px;top:127.5px;width:197.5px;height:507.5px;background:var(--soft)}
.side-item{position:absolute;left:20px;right:12px;font-size:10px;font-weight:500;display:flex;justify-content:space-between;align-items:center}
.side-active{position:absolute;left:0;top:0;width:197.5px;height:25.5px;background:var(--brand);color:var(--white);font-size:10px;font-weight:500;padding:8px 0 0 20px}
.panel{position:absolute;left:392.5px;width:632.5px;background:var(--white);border:1px solid #e6e6e6;border-top:6px solid var(--brand);border-radius:3px;box-shadow:0 1px 3px rgba(0,0,0,.06)}
.panel-title{font-size:12.5px;font-weight:500}
.label{font-size:8.75px;font-weight:500}
.field{width:150px;height:19px;border:1px solid var(--line);border-radius:3px;background:var(--white);font-size:8px;color:var(--muted);padding:5px 7px;display:flex;justify-content:space-between;align-items:center}
.btn{background:var(--brand);color:var(--white);font-size:8.75px;font-weight:700;border-radius:3px;display:flex;align-items:center;justify-content:center}
.select-small{width:54px;height:15.5px;border:1px solid var(--line);border-radius:3px;font-size:7.5px;color:var(--muted);padding:3px 5px;display:flex;justify-content:space-between;align-items:center}
.plus-box{width:15px;height:15px;border:1px solid var(--line);border-radius:3px;display:flex;align-items:center;justify-content:center;color:var(--muted);font-size:11px}
.domain-table{left:20px;top:80.5px;width:593.5px;height:120px;border:1px solid var(--line);border-radius:3px;overflow:hidden}
.table-head{height:29.5px;background:var(--soft);border-bottom:1px solid var(--line);font-size:8.75px;font-weight:500;position:relative}
.row{position:relative;height:30px;border-bottom:1px solid var(--line);font-size:8.75px}
.row:last-child{border-bottom:none}
.check{position:absolute;left:10px;top:10px;width:10px;height:10px;border:1px solid #b5b5b5;border-radius:2px}
.dots{position:absolute;left:29.5px;top:12.5px;display:flex;gap:3.8px}
.dots i{display:block;width:5px;height:5px;border-radius:50%;border:1px solid var(--line)}
.dots i.on{background:var(--ok);border-color:var(--ok)}
.dom{position:absolute;left:71px;top:10px;display:flex;align-items:center;gap:10px}
.tag{font-size:5px;font-weight:700;color:var(--ok);border:1px solid var(--ok);border-radius:6px;padding:1px 4px}
.actions{position:absolute;right:12px;top:9px;display:flex;gap:9px;align-items:center}
</style>
</head>
<body>
<div class="canvas">

  <header class="topbar">
    <div class="abs brand-name">Domora</div>
    <div class="abs notice" style="left:610px;top:15px">
      <svg width="10" height="8" viewBox="0 0 10 8"><rect width="10" height="8" rx="1" fill="#fff"/><path d="M0.5 1 L5 4.5 L9.5 1" stroke="#e11d27" fill="none" stroke-width="1"/></svg>
      neue Nachrichten</div>
    <div class="abs notice" style="left:610px;top:30px">
      <svg width="10" height="10" viewBox="0 0 10 10"><circle cx="5" cy="5" r="5" fill="#fff"/><path d="M5 2.2 V5 H7.2" stroke="#e11d27" fill="none" stroke-width="1.2"/></svg>
      Aufragsstapel</div>
    <div class="abs meta" style="left:816px;top:15px">Version: 2.2.8</div>
    <div class="abs meta" style="left:879px;top:15px">Sitemap</div>
    <div class="abs session-user" style="left:941px;top:15px">angemeldet als karla</div>
    <div class="abs session-bar"><span></span></div>
    <div class="abs session-rest" style="left:941px;top:40px">120 min. Restzeit</div>
    <div class="abs logout" style="left:1127px;top:27px">
      <svg width="11" height="10" viewBox="0 0 11 10"><path d="M6 1 H1 V9 H6" stroke="#fff" fill="none" stroke-width="1.2"/><path d="M4 5 H10 M8 3 L10 5 L8 7" stroke="#fff" fill="none" stroke-width="1.2"/></svg>
      Logout</div>
  </header>

  <nav class="mainnav">
    <a style="left:474px">Start</a>
    <a style="left:523px">Benutzer</a>
    <a style="left:588px">Kontakt</a>
    <a class="active" style="left:649px">Domain</a>
    <a style="left:709px">DNS</a>
  </nav>

  <aside class="abs sidebar">
    <div class="side-active">Domain Liste</div>
    <div class="side-item" style="top:38px">Domain registrieren</div>
    <div class="side-item" style="top:69px">Domain transferieren</div>
    <div class="side-item" style="top:99.5px">Domain bearbeiten</div>
    <div class="side-item" style="top:130px">Domain wiederherstellen</div>
    <div class="side-item" style="top:161px">Messenaufrage</div>
    <div class="side-item" style="top:191px">DNSSEC <svg width="8" height="5" viewBox="0 0 8 5"><path d="M1 1 L4 4 L7 1" stroke="#1c1c1c" fill="none" stroke-width="1.2"/></svg></div>
    <div class="side-item" style="top:222px">Werkzeug <svg width="8" height="5" viewBox="0 0 8 5"><path d="M1 1 L4 4 L7 1" stroke="#1c1c1c" fill="none" stroke-width="1.2"/></svg></div>
  </aside>

  <section class="panel filter" style="top:127.5px;height:223.5px">
    <div class="abs panel-title" style="left:20px;top:16px">Listen-Filter</div>
    <div class="abs meta" style="left:398px;top:21px;font-size:8.5px">Zeilen pro siete</div>
    <div class="abs select-small" style="left:462.5px;top:18px">- <svg width="7" height="4" viewBox="0 0 7 4"><path d="M1 .5 L3.5 3 L6 .5" stroke="#888" fill="none"/></svg></div>
    <div class="abs meta" style="left:528px;top:21px;font-size:8.5px">Wreiter optionen</div>
    <div class="abs plus-box" style="left:597.5px;top:17px">+</div>

    <div class="abs label" style="left:20px;top:60px">Domain*</div>
    <div class="abs field" style="left:112.5px;top:50.5px"></div>
    <div class="abs label" style="left:20px;top:89px">Benutzer*</div>
    <div class="abs field" style="left:112.5px;top:80px"><span></span><svg width="7" height="4" viewBox="0 0 7 4"><path d="M1 .5 L3.5 3 L6 .5" stroke="#1c1c1c" fill="none"/></svg></div>
    <div class="abs label" style="left:20px;top:118.5px">Renewal-Mode*</div>
    <div class="abs field" style="left:112.5px;top:109px"><span></span><svg width="7" height="4" viewBox="0 0 7 4"><path d="M1 .5 L3.5 3 L6 .5" stroke="#1c1c1c" fill="none"/></svg></div>
    <div class="abs label" style="left:20px;top:148px">Expire On*</div>
    <div class="abs field" style="left:112.5px;top:138.5px">DD/MM/YYYY</div>

    <div class="abs label" style="left:371.5px;top:60px">Umlautdomain*</div>
    <div class="abs field" style="left:462.5px;top:50.5px"></div>
    <div class="abs label" style="left:371.5px;top:88.5px">Kontakt*</div>
    <div class="abs field" style="left:462.5px;top:79.5px"></div>
    <div class="abs label" style="left:371.5px;top:117.5px">Lock-Status*</div>
    <div class="abs field" style="left:462.5px;top:108.5px"></div>
    <div class="abs label" style="left:371.5px;top:146px">bis*</div>
    <div class="abs field" style="left:462.5px;top:137px">DD/MM/YYYY</div>

    <div class="abs btn" style="left:501.5px;top:175.5px;width:110.5px;height:22px">Domains auflisten</div>
  </section>

  <section class="panel list" style="top:371px;height:264px">
    <div class="abs panel-title" style="left:20px;top:16px">Liste</div>
    <div class="abs label" style="right:19px;top:17px">Export CSV</div>
    <div class="abs label" style="left:20px;top:44.5px">3 Elemente</div>
    <div class="abs field" style="left:91.5px;top:35px;width:251px;color:var(--ink);font-size:8.75px">neuedesign-domora.com - tesdomain-domora.com... <svg width="7" height="4" viewBox="0 0 7 4"><path d="M1 .5 L3.5 3 L6 .5" stroke="#1c1c1c" fill="none"/></svg></div>

    <div class="abs domain-table">
      <div class="table-head">
        <span class="abs" style="left:9.5px;top:10px">Status</span>
        <span class="abs" style="left:71px;top:10px">Domain</span>
      </div>
      <div class="row"><span class="check"></span><span class="dots"><i></i><i></i><i class="on"></i></span><span class="dom">neuesdesign-domora.com <span class="tag">Neu!</span></span>
        <span class="actions">
          <svg width="11" height="10" viewBox="0 0 11 10"><rect x=".5" y="1.5" width="8" height="8" fill="none" stroke="#777"/><path d="M4 6 L10 0.5" stroke="#777" stroke-width="1.4"/></svg>
          <svg width="11" height="10" viewBox="0 0 11 10"><path d="M2 5 A4 4 0 1 0 3.5 2" fill="none" stroke="#777"/><path d="M1 1.5 L3.5 2 L3 4.5" fill="none" stroke="#777"/><path d="M6 3 V5.5 H8" fill="none" stroke="#777"/></svg>
          <svg width="4" height="10" viewBox="0 0 4 10"><circle cx="2" cy="1.2" r="1.2" fill="#777"/><rect x="1" y="3.5" width="2" height="6.5" fill="#777"/></svg>
        </span></div>
      <div class="row"><span class="check"></span><span class="dots"><i></i><i></i><i class="on"></i></span><span class="dom">test-domora.com <span class="tag">Neu!</span></span>
        <span class="actions">
          <svg width="11" height="10" viewBox="0 0 11 10"><rect x=".5" y="1.5" width="8" height="8" fill="none" stroke="#777"/><path d="M4 6 L10 0.5" stroke="#777" stroke-width="1.4"/></svg>
          <svg width="11" height="10" viewBox="0 0 11 10"><path d="M2 5 A4 4 0 1 0 3.5 2" fill="none" stroke="#777"/><path d="M1 1.5 L3.5 2 L3 4.5" fill="none" stroke="#777"/><path d="M6 3 V5.5 H8" fill="none" stroke="#777"/></svg>
          <svg width="4" height="10" viewBox="0 0 4 10"><circle cx="2" cy="1.2" r="1.2" fill="#777"/><rect x="1" y="3.5" width="2" height="6.5" fill="#777"/></svg>
        </span></div>
      <div class="row"><span class="check"></span><span class="dots"><i></i><i></i><i class="on"></i></span><span class="dom">testdomain-domora.com <span class="tag">Neu!</span></span>
        <span class="actions">
          <svg width="11" height="10" viewBox="0 0 11 10"><rect x=".5" y="1.5" width="8" height="8" fill="none" stroke="#777"/><path d="M4 6 L10 0.5" stroke="#777" stroke-width="1.4"/></svg>
          <svg width="11" height="10" viewBox="0 0 11 10"><path d="M2 5 A4 4 0 1 0 3.5 2" fill="none" stroke="#777"/><path d="M1 1.5 L3.5 2 L3 4.5" fill="none" stroke="#777"/><path d="M6 3 V5.5 H8" fill="none" stroke="#777"/></svg>
          <svg width="4" height="10" viewBox="0 0 4 10"><circle cx="2" cy="1.2" r="1.2" fill="#777"/><rect x="1" y="3.5" width="2" height="6.5" fill="#777"/></svg>
        </span></div>
    </div>

    <div class="abs btn" style="left:514px;top:215.5px;width:99.5px;height:22px">Massenauftrag</div>
  </section>

</div>
</body>
</html>
```